Building Servicess

We need a new business card design for a company. We specialise in: Electrical/Site temporary electrics, Data/Network Installation, Passive Fire Protection

Industry/Entity Type

Construction

Contact Information for Business Card

Services provided as detailed on project description

Font styles to use
Serif

Colors
0054AA
0677BA
7BADD7
CADEEF
E8F1F8
00AB8E
00BBA5
67D7C9
C6EFE9
E9F9F6
EB3D1F
EC4F4E
F09395
F8D3D4
FCEDEE

Requirements
Must have
• Company logo-contact details-phone numbers

```html
<!DOCTYPE html>
<html lang="en">
<head>
<meta charset="utf-8">
<title>Hartwell Site Services – Business Card</title>
<link rel="stylesheet" href="https://fonts.googleapis.com/css2?family=Roboto:wght@400;700&display=swap">
<style>
  :root {
    --blue: #0d77bd;
    --ink: #231f20;
    --rule: #808285;
    --paper: #ffffff;
    --backdrop: #d8d8d8;
  }
  * { margin: 0; padding: 0; box-sizing: border-box; }
  html, body { width: 1200px; height: 1059px; overflow: hidden; }
  body {
    position: relative;
    background: var(--backdrop);
    font-family: "Roboto", Arial, sans-serif;
    color: var(--ink);
  }
  .card {
    position: absolute;
    width: 690px;
    height: 393px;
    border-radius: 18px;
  }
  .card--front { left: 255px; top: 100px; background: var(--paper); }
  .card--back  { left: 255px; top: 537px; background: var(--blue); }

  .brand {
    position: absolute;
    display: flex;
    align-items: center;
    font-weight: 700;
    letter-spacing: 0.5px;
    line-height: 1.05;
    text-transform: uppercase;
  }
  .brand__square { flex: none; }
  .card--front .brand {
    left: 34px; top: 142px;
    width: 300px;
    color: var(--blue);
    font-size: 27px;
    gap: 14px;
  }
  .card--front .brand__square { width: 44px; height: 44px; background: var(--blue); }
  .card--back .brand {
    left: 0; right: 0; top: 150px;
    justify-content: center;
    color: var(--paper);
    font-size: 44px;
    gap: 22px;
  }
  .card--back .brand__square { width: 70px; height: 70px; background: var(--paper); }

  .divider {
    position: absolute;
    left: 345px; top: 98px;
    width: 1.5px; height: 196px;
    background: var(--rule);
  }
  .details { position: absolute; left: 372px; top: 97px; }
  .person__name {
    color: var(--blue);
    font-weight: 700;
    font-size: 24px;
    letter-spacing: 0.3px;
    line-height: 1;
  }
  .person__role { font-size: 15.5px; margin-top: 4px; margin-left: 1px; }
  .address { font-size: 15.5px; line-height: 21px; margin-top: 23px; }
  .contact { list-style: none; margin-top: 9px; font-size: 15.5px; }
  .contact li { display: flex; align-items: center; height: 20.7px; gap: 6px; }
  .contact svg { width: 12px; height: 12px; flex: none; }
</style>
</head>
<body>
  <section class="card card--front">
    <div class="brand">
      <span class="brand__square"></span>
      <span class="brand__name">Hartwell<br>Site Services</span>
    </div>
    <div class="divider"></div>
    <div class="details">
      <h1 class="person__name">MAREK DOBROWSKI</h1>
      <p class="person__role">Managing Director</p>
      <p class="address">418 Westbrook Mill Road.<br>Kingsford, AB 50312</p>
      <ul class="contact">
        <li>
          <svg viewBox="0 0 12 12" aria-hidden="true"><rect x="3" y="0.7" width="6" height="10.6" rx="1.2" fill="none" stroke="#0d77bd" stroke-width="1.2"/><circle cx="6" cy="9.4" r="0.7" fill="#0d77bd"/></svg>
          07700900412
        </li>
        <li>
          <svg viewBox="0 0 12 12" aria-hidden="true"><path d="M2.2 1.2 L4.3 1 L5.2 3.6 L3.9 4.6 Q5 7 7.4 8.1 L8.4 6.8 L11 7.7 L10.8 9.8 Q10.3 11 8.8 10.9 Q2.5 10 1.1 3.2 Q1 1.7 2.2 1.2 Z" fill="#0d77bd"/></svg>
          020 7946 0831
        </li>
        <li>
          <svg viewBox="0 0 12 12" aria-hidden="true"><rect x="0.5" y="2.3" width="11" height="7.6" rx="0.8" fill="#0d77bd"/><path d="M1 3 L6 6.6 L11 3" fill="none" stroke="#fff" stroke-width="1"/></svg>
          info@hartwellsiteservices.com
        </li>
        <li>
          <svg viewBox="0 0 12 12" aria-hidden="true"><circle cx="6" cy="6" r="5.3" fill="#0d77bd"/><path d="M0.9 6 H11.1 M6 0.7 Q3 6 6 11.3 M6 0.7 Q9 6 6 11.3" fill="none" stroke="#fff" stroke-width="0.8"/></svg>
          www.hartwellsiteservices.com
        </li>
      </ul>
    </div>
  </section>

  <section class="card card--back">
    <div class="brand">
      <span class="brand__square"></span>
      <span class="brand__name">Hartwell<br>Site Services</span>
    </div>
  </section>
</body>
</html>
```